Velora Bright Days introduciendo 432Plaza.com

We need the name of the event look like a trade mark. for other activities or events.
"Velora Bright Days" the part of introducing 432plaza could be lower so people only can relate to that.

We need a flyer design for an event is a Bazar where our principal comunication target are the consumer but stores will be atracted to it with this same flyer.....

the graphic disign could be abstract clean backgrown more focus on the name of the event. information font is not what we want to predominate on this. is more about some modern and elegant disign.

We need a flyer design for an event is a Bazar where our stores and customer will interact eachother, this day people will know more about what is 432plaza for the dominican republic market, its like the firts orvina local where individuals and businesses can sell products anywhere in de country. but this 432plaza in our comunication is secundary.......we need people focus o the Bazar. the Logo of 432plaza could be there small.

This event have the purpuse to atract both target our stores vendors and the general public where they can enjoy a nice sunday shopping day from 11am to 10pm, this event will take place indoor and outdoor location where the offices of 432plaza are,. its a mall where inside the offices we will have many stores selling as well outside, djs playin live and food placements where clients can rest and enjoy the day.

We name this Bazaar Velora Bright Days introducing 432plaza because we want to take this event to diferents cities to afiliate stores in to this new plataform so they can open there stores online with us and at the same time promote the site with the whole country as a marketing effort.

Target Market(s)

Young adult between 18 and 35

Industry/Entity Type

Marketing

Font styles to use
Serif

Requirements
Must have
• Fresh and modern look.

```html
<!DOCTYPE html>
<html lang="es">
<head>
<meta charset="utf-8">
<title>Velora Bright Days – 432Plaza</title>
<link rel="stylesheet" href="https://fonts.googleapis.com/css2?family=Oswald:wght@400;500;700&family=Montserrat:wght@700;800&family=Orbitron:wght@600&family=Arvo:wght@700&family=Rokkitt:wght@800;900&family=Bebas+Neue&display=swap">
<style>
  :root{
    --backdrop:#6e6e6e;
    --cream:#fcf6d6;
    --cream-light:#fffdf0;
    --ink:#111111;
    --red:#d4200f;
    --deep-red:#a8160a;
    --orange:#ff5a12;
    --amber:#ff9c00;
    --sun:#ffd21a;
    --white:#ffffff;
  }
  *{margin:0;padding:0;box-sizing:border-box}
  html,body{width:1200px;height:907px;overflow:hidden;background:var(--backdrop)}
  .flyer{
    position:absolute;left:88px;top:86px;width:1010px;height:740px;overflow:hidden;
    background:radial-gradient(ellipse at 60% 40%,var(--cream-light) 0%,var(--cream) 70%);
  }
  .flyer-art{position:absolute;left:0;top:0;width:1010px;height:740px}
  .event-title{
    position:absolute;right:32px;top:52px;
    font-family:"Oswald",sans-serif;font-weight:700;font-size:93px;line-height:1;
    letter-spacing:-1px;color:var(--ink);white-space:nowrap;
  }
  .event-title .accent{color:var(--red)}
  .tagline{
    position:absolute;right:32px;top:170px;
    font-family:"Montserrat",sans-serif;font-weight:800;font-size:16.5px;color:var(--red);white-space:nowrap;
  }
  .host{
    position:absolute;right:32px;top:202px;
    font-family:"Orbitron",sans-serif;font-weight:600;font-size:19px;letter-spacing:1px;color:var(--ink);
  }
  .date{
    position:absolute;right:32px;top:238px;
    font-family:"Arvo",serif;font-weight:700;font-size:19px;text-transform:uppercase;white-space:nowrap;
  }
  .date .day{color:var(--orange);text-shadow:1px 1px 1px rgba(0,0,0,.6)}
  .date .num{color:var(--ink)}
  .date .month{
    color:var(--white);
    text-shadow:1px 1px 0 #2a2a2a,-1px 0 0 #555,0 -1px 0 #555,2px 2px 2px rgba(0,0,0,.6);
  }
  .details{
    position:absolute;right:32px;top:274px;text-align:right;
    font-family:"Oswald",sans-serif;font-weight:500;font-size:20px;line-height:34px;
    text-transform:uppercase;color:var(--ink);white-space:nowrap;
  }
  .details .value{color:var(--deep-red)}
  .guest-band{
    position:absolute;left:427px;top:378px;width:583px;height:278px;
    background:linear-gradient(90deg,rgba(255,90,18,0) 0%,rgba(255,90,18,.75) 22%,var(--orange) 45%);
  }
  .guest-label{
    position:absolute;right:32px;top:392px;
    font-family:"Rokkitt",serif;font-weight:800;font-size:66px;line-height:1.1;
    color:var(--white);text-shadow:2px 3px 4px rgba(0,0,0,.45);white-space:nowrap;
  }
  .guest-name{
    position:absolute;right:32px;top:466px;
    font-family:"Rokkitt",serif;font-weight:900;font-size:112px;line-height:1;
    color:var(--amber);text-shadow:2px 3px 4px rgba(0,0,0,.4);white-space:nowrap;
  }
  .happy-hour{
    position:absolute;right:32px;top:594px;
    font-family:"Bebas Neue",sans-serif;font-size:48px;color:var(--ink);white-space:nowrap;
  }
  .brand{
    position:absolute;right:30px;top:670px;display:flex;align-items:center;gap:10px;
    font-family:"Montserrat",sans-serif;font-weight:700;font-size:26px;color:var(--orange);
  }
  .brand-square{width:28px;height:28px;background:var(--amber);border-radius:4px}
  .brand-rule{width:2px;height:34px;background:#555;margin-left:6px}
  .invite-badge{position:absolute;left:40px;top:466px;width:200px;height:190px}
  .invite-badge .ray{position:absolute;inset:18px;background:var(--red)}
  .invite-badge .ray:nth-child(2){transform:rotate(22.5deg)}
  .invite-badge .ray:nth-child(3){transform:rotate(45deg)}
  .invite-badge .ray:nth-child(4){transform:rotate(67.5deg)}
  .invite-badge .core{
    position:absolute;inset:22px;border-radius:50%;
    background:radial-gradient(circle at 50% 30%,#f0463a 0%,var(--red) 45%,var(--deep-red) 100%);
  }
  .invite-text{
    position:absolute;inset:0;display:flex;flex-direction:column;align-items:center;justify-content:center;
    font-family:"Montserrat",sans-serif;font-weight:800;font-size:30px;line-height:1.35;color:var(--white);
  }
</style>
</head>
<body>
<main class="flyer">
  <svg class="flyer-art" viewBox="0 0 1010 740">
    <defs>
      <radialGradient id="sunGlow" cx="0" cy="0.4" r="0.9">
        <stop offset="0" stop-color="#ffd21a"/>
        <stop offset="0.35" stop-color="#ffa000"/>
        <stop offset="1" stop-color="#ff6a00"/>
      </radialGradient>
    </defs>
    <path role="img" aria-label="Orange sunburst backdrop" d="M0,0 L240,0 C140,200 110,500 420,740 L0,740 Z" fill="url(#sunGlow)"/>
    <path class="swoosh-band" d="M258,-10 C140,200 120,500 445,750" fill="none" stroke="#c8200c" stroke-width="34"/>
    <path class="swoosh-line" d="M228,0 C250,60 262,100 282,140 C320,210 360,300 370,400 C380,500 372,600 385,660 C392,700 396,720 402,740" fill="none" stroke="#111" stroke-width="3"/>
    <path class="swoosh-line-thin" d="M205,40 C280,110 300,180 285,260 C270,340 300,420 330,500 C350,560 325,650 330,740" fill="none" stroke="#c45a4a" stroke-width="1.2"/>
  </svg>

  <h1 class="event-title">Velora Bright <span class="accent">Days</span></h1>
  <p class="tagline">Acompañanos y disfruta de una manera diferente de comprar!!</p>
  <p class="host">432PLAZA</p>
  <p class="date"><span class="day">Domingo</span> <span class="num">30</span> <span class="month">Noviembre</span></p>
  <p class="details">
    Hora: <span class="value">Desde 11am a 10pm</span><br>
    Donde: <span class="value">Plaza Coralina, Ave. Las</span><br>
    <span class="value">Palmas esq. Del Sol</span>
  </p>

  <div class="guest-band"></div>
  <p class="guest-label">Invitado especial</p>
  <p class="guest-name">DJ SOLANO</p>
  <p class="happy-hour">Happy hour desde las 4:30pm</p>

  <div class="brand"><span class="brand-square"></span><span>432plaza</span><span class="brand-rule"></span></div>

  <div class="invite-badge">
    <span class="ray"></span><span class="ray"></span><span class="ray"></span><span class="ray"></span>
    <span class="core"></span>
    <p class="invite-text"><span>SE LE</span><span>INVITA</span></p>
  </div>
</main>
</body>
</html>
```